Corporate Design für einen Rebell in der Gesundheitsbranche
Zielgruppe
Wir denken Gesundheit neu. Wir räumen mit Althergebrachtem auf und helfen den Menschen, sich wieder aktiv um ihre Gesundheit zu kümmern.
Unser Unternehmen entwickelt, produziert und vertreibt Produkte mit denen Menschen ihre Gesundheit erhalten, verbessern oder wiederherstellen können.
Die Produkte sind für Endverbraucher bestimmt, der Vertrieb erfolgt als B2B an Schuhfabrikanten, große Schuhhäuser und Orthopädiefachgeschäfte sowohl in Deutschland als auch international.
Dabei sind die zentralen Elemente
1. Fußgesundheit und Körperhaltung: aktivierende Schuh-Einlagen, Haltungs-, Gang- und Laufanalysen
2. Einsatz von moderner Technologie (3D Scans, Sensorik, Videoanalse, Ergometer)
3. Produktentwicklung basiert auf aktuellen Forschungsergebnissen im Bereich Neuro-Physiologie und Sensomotorik.
Das erste zentrale Produkt, welches kurz vor der Markteinführung steht ist die Vela Trimo Base(R), eine patentierte sensomotorische Einlage, die über eine neuro-physiologische Wirkungsweise die Fußgesundheit verbessern kann und Haltungsbeschwerden sowie -schmerzen reduziert.
Das gesamte Produktkonzept basiert auf einem neuen, zukunftsweisenden Verständnis der Zusammenhänge zwischen Muskeln, Bindegewebe, Füßen, Neurophysiologie, Wissenschaft und Medizin.
Das Design sollte vor allem Erwachsenen gefallen und Gesundheit, Innovation Ganzheitlichkeit vermitteln.
Aufgabenstellung
Das Logo sollte folgende Komponenten enthalten: Gehirn, Fuß oder Füße, Dreieck.
Gehirn: Neurophysiologie
Fuß: Fundament der Haltung
Dreieck: Basiselement in der Architektur (Tensegrity-Modell)
Das Design sollte stilisierend sein. Die drei Elemente sollten mit möglichst wenigen stilisierenden Federstrichen erkennbar sein.
Das Logo sollte vom Firmennamen abtrennbar sein, um es separat zur Wiedererkennung zu nutzen, auch ohne Firmenname.
Seriosität und Schnörkellosigkeit ist ein wichtiger Aspekt. Wir sehen unsere Firma aber auch als Rebell, da wir die vorherrschende Meinung in der Orthopädie grundlegend umkrempeln werden.
Wir möchten also auch Innovation, Wissenschaftlichkeit und eine neue Art über Gesundheit zu denken mit dem Design vermitteln.

```html
<!DOCTYPE html>
<html lang="de">
<head>
<meta charset="utf-8">
<title>Halvora – Corporate Design</title>
<link href="https://fonts.googleapis.com/css2?family=Lato:wght@400;700&family=Merriweather:wght@700&display=swap" rel="stylesheet">
<style>
  :root {
    --teal-light: #b6eef1;
    --teal-mid: #8adde2;
    --teal-dark: #62c6cd;
    --ink: #1a1a1a;
    --text: #3a3a3a;
    --muted: #8a8a8a;
    --paper: #ffffff;
    --ground: #e6e6e4;
  }
  * { box-sizing: border-box; margin: 0; padding: 0; }
  html, body { width: 922px; height: 1200px; overflow: hidden; }
  body { position: relative; background: var(--ground); font-family: "Lato", sans-serif; color: var(--text); }

  .brand-stage { position: absolute; left: 0; top: 0; width: 922px; height: 454px; background: var(--paper); overflow: hidden; }
  .band { position: absolute; }

  .wordmark { position: absolute; display: flex; align-items: center; font-family: "Lato", sans-serif; font-weight: 700; color: var(--ink); line-height: 1; white-space: nowrap; }
  .wordmark .mark { background: var(--teal-dark); flex: none; }
  .wordmark--hero { left: 50%; top: 190px; transform: translateX(-50%); gap: 22px; font-size: 72px; letter-spacing: 2px; }
  .wordmark--hero .mark { width: 40px; height: 40px; }

  .letterhead { position: absolute; left: 115px; top: 490px; width: 486px; height: 678px; background: var(--paper); overflow: hidden; }
  .letterhead .wordmark { right: 40px; top: 44px; gap: 8px; font-size: 22px; letter-spacing: 1px; }
  .letterhead .wordmark .mark { width: 12px; height: 12px; }
  .sender-line { position: absolute; left: 56px; top: 104px; font-size: 6px; color: var(--muted); }
  .recipient { position: absolute; left: 56px; top: 140px; font-size: 10px; line-height: 1.55; font-style: normal; }
  .recipient strong, .subject { font-weight: 700; color: var(--ink); }
  .subject { position: absolute; left: 56px; top: 224px; font-size: 10px; }
  .letter-body { position: absolute; left: 56px; top: 274px; width: 405px; font-size: 9px; line-height: 1.6; }
  .letter-body p { margin-bottom: 12px; }
  .letter-footer { position: absolute; left: 0; bottom: 0; width: 486px; height: 60px; background: var(--teal-light); border-top: 6px solid var(--teal-dark); }
  .footer-cols { position: absolute; left: 56px; bottom: 14px; display: flex; gap: 30px; font-size: 5.5px; line-height: 1.45; color: var(--text); }

  .card { position: absolute; width: 214px; height: 124px; background: var(--paper); overflow: hidden; }
  .card--back { left: 640px; top: 560px; }
  .card--front { left: 664px; top: 780px; }
  .card .wordmark { right: 16px; top: 22px; gap: 6px; font-size: 17px; letter-spacing: 1px; }
  .card .wordmark .mark { width: 9px; height: 9px; }
  .card-name { position: absolute; left: 20px; top: 56px; font-family: "Merriweather", serif; font-weight: 700; font-size: 9.5px; color: var(--ink); }
  .card-role { position: absolute; left: 20px; top: 70px; font-size: 6.5px; }
  .card-foot { position: absolute; left: 0; bottom: 0; width: 214px; height: 34px; background: var(--teal-light); border-top: 3px solid var(--teal-dark); }
  .card-contact { position: absolute; left: 20px; bottom: 6px; display: flex; gap: 26px; font-size: 5px; line-height: 1.4; }
</style>
</head>
<body>

<section class="brand-stage">
  <div class="band" style="right:0;top:0;width:380px;height:14px;background:var(--teal-light)"></div>
  <div class="band" style="right:0;top:22px;width:240px;height:8px;background:var(--teal-dark)"></div>
  <div class="band" style="left:0;bottom:40px;width:160px;height:8px;background:var(--teal-dark)"></div>
  <div class="band" style="left:0;bottom:0;width:260px;height:26px;background:var(--teal-light)"></div>
  <div class="wordmark wordmark--hero"><span class="mark"></span><span>Halvora</span></div>
</section>

<article class="letterhead">
  <div class="wordmark"><span class="mark"></span><span>Halvora</span></div>
  <p class="sender-line">Halvora, Musterstraße 123, 12345 Musterstadt</p>
  <address class="recipient">
    <strong>Musterfirma</strong><br>Max Mustermann<br>Musterstraße 16<br>12345 Musterstadt
  </address>
  <p class="subject">Osandit re corrovi dellore mporro dolupta voluptiisto</p>
  <div class="letter-body">
    <p>Te commos exero deriatiasit magnis,</p>
    <p>magnimin cus ad ut eaquamus eum rem. Rem. Et aribea velestrum et, que voluptatur audia inverunto magnimi, qui coris core abo. Riae nos enima vide veliquame ommos ant ommoluptat ex essimi, quae doloriate porrumqui apiende leniate mporro berum alit molo magnihilit, cust voloruptat lautem invenem qui odit vit odipsusci deliquam es molest lia dis as eum, qui volupta tquiam illantiat.</p>
    <p>Ugiae omni aut que nullis expland icaborest ut veruptaquiae estorro viduci sum eost arum experib ersperem nis rerum sit, vollorerum qui assitius doluptaectur sit voloribus, volesci psandi blabore mporrerum int remporum nis simus aut eaquiscide se voles exped millore catetusciis et ea non re dolum sandus.</p>
    <p>Ihitist ut que pe prepers peliquam,</p>
  </div>
  <div class="letter-footer"></div>
  <div class="footer-cols">
    <p>Halvora<br>Musterstraße 123<br>12345 Musterstadt</p>
    <p>Sitz der Gesellschaft: Musterstadt<br>Registergericht: Amtsgericht Musterstadt<br>Handelsregisternummer: XXX 123456</p>
    <p>Geschäftsführer: Max Mustermann<br>USt-ID-Nr.: DE 123456789<br>www.website.de</p>
  </div>
</article>

<div class="card card--back">
  <div class="band" style="left:0;top:0;width:214px;height:10px;background:var(--teal-dark)"></div>
  <div class="band" style="left:0;bottom:0;width:214px;height:40px;background:var(--teal-light)"></div>
</div>

<div class="card card--front">
  <div class="wordmark"><span class="mark"></span><span>Halvora</span></div>
  <p class="card-name">Max Mustermann</p>
  <p class="card-role">Position</p>
  <div class="card-foot"></div>
  <div class="card-contact">
    <p>Hauptstraße 123<br>12345 Hauptstadt<br>halvora.de</p>
    <p>T: 0123 456789<br>M: 0123 456780<br>kontakt@halvora.de</p>
  </div>
</div>

</body>
</html>
```